Fiber Optic Internet flyer promotion Winter 2016-2017

I am looking for a marketing flyer that will not be folded, single sided that will advertise a Fiber Optic internet promotion that we are currently running.

The design should be clean, flow well, quickly grab attention, and if a very few short seconds list what the promotion is, and direct them to contact us.

It needs to list a few features of the promotion, but does not need to be in this order and should flow well with the flyer
1.) Fiber Optic Internet
2.) 100 Mbits for $140 /month or 150 Mbits for $190 /month
3.) Free construction cost up to $10,000, limited funds available.
4.) Limited time offer. Must commit before funds run out.

(555) 274-3916, www.kelvoranet.example

Target Market(s)

Small to large business

Industry/Entity Type

Internet Service Provider

Requirements
Must have
• Eye catching appeal. Quickly convey the message of the promotion and our company name and phone number.
Should not have
• Our company is primarily a wireless ISP. This promotion is all about Fiber Optic. I do not want to draw attention to the "wireless" portion of our business with this flyer.

```html
<!DOCTYPE html>
<html lang="en">
<head>
<meta charset="utf-8">
<title>Fiber Optic Internet Flyer</title>
<link rel="stylesheet" href="https://fonts.googleapis.com/css2?family=Lato:ital,wght@0,400;0,700;0,900;1,400&display=swap">
<style>
  :root {
    --page-bg: #ececec;
    --paper: #ffffff;
    --red: #d0202f;
    --navy: #14267f;
    --steel-dark: #6e6e6e;
    --steel-mid: #b4b4b4;
    --steel-light: #f2f2f2;
  }
  * { margin: 0; padding: 0; box-sizing: border-box; }
  html, body {
    width: 1200px; height: 1000px; overflow: hidden;
    background: var(--page-bg);
    font-family: "Lato", Arial, sans-serif;
  }
  .flyer {
    position: absolute; left: 338px; top: 120px;
    width: 532px; height: 752px;
    background: var(--paper);
    overflow: hidden;
  }
  .hero-visual {
    position: absolute; left: 0; top: 380px; width: 532px; height: 340px;
    background: linear-gradient(180deg, var(--steel-light) 0%, var(--steel-mid) 35%, var(--steel-dark) 60%, var(--steel-light) 88%, var(--paper) 100%);
  }
  .headline {
    position: absolute; left: 0; width: 100%;
    text-align: center; font-weight: 900; letter-spacing: 1px; line-height: 1;
  }
  .headline--fiber { top: 38px; font-size: 64px; color: var(--red); }
  .headline--internet { top: 110px; font-size: 68px; color: var(--navy); }
  .pricing {
    position: absolute; top: 188px; left: 0; width: 100%;
    text-align: center; color: var(--red); font-weight: 700;
    font-size: 30px; line-height: 46px;
  }
  .offer {
    position: absolute; top: 286px; left: 0; width: 100%;
    text-align: center; color: var(--navy);
  }
  .offer__title { font-weight: 900; font-size: 21px; line-height: 26px; }
  .offer__note { font-size: 15px; line-height: 22px; }
  .offer__note--italic { font-style: italic; }
  .brand {
    position: absolute; left: 26px; top: 672px;
    display: flex; align-items: center; gap: 10px;
    color: var(--navy); font-weight: 900; font-size: 24px; letter-spacing: 1px;
  }
  .brand__mark {
    width: 16px; height: 16px; border-radius: 50%; background: var(--red);
  }
  .contact {
    position: absolute; right: 20px; top: 640px;
    text-align: right;
  }
  .contact__cta { color: var(--navy); font-weight: 700; font-size: 19px; line-height: 26px; }
  .contact__phone { color: var(--red); font-weight: 700; font-size: 35px; line-height: 44px; }
  .contact__web { color: var(--navy); font-size: 19px; line-height: 26px; letter-spacing: 0.5px; }
</style>
</head>
<body>
  <main class="flyer">
    <div class="hero-visual" role="img" aria-label="Metallic house shapes with blue fiber optic connectors and a cyan fiber optic cable plugged in"></div>

    <h1 class="headline headline--fiber">FIBER OPTIC</h1>
    <h2 class="headline headline--internet">INTERNET</h2>

    <p class="pricing">100 Mbits for $140 /month or<br>150 Mbits for $190 /month</p>

    <div class="offer">
      <p class="offer__title">LIMITED TIME OFFER</p>
      <p class="offer__note">Must commit before funds run out</p>
      <p class="offer__note offer__note--italic">Free construction cost up to $10,000, limited funds available.</p>
    </div>

    <div class="brand">
      <span class="brand__mark"></span>
      <span class="brand__name">KELVORA NET</span>
    </div>

    <div class="contact">
      <p class="contact__cta">Get It Today! Call Us</p>
      <p class="contact__phone">(555) 274-3916</p>
      <p class="contact__web">www.kelvoranet.example</p>
    </div>
  </main>
</body>
</html>
```